Business card for Sports Apparel business

DOUBLE SIDED DESIGN
We need business cards for a new sports apparel business. We are developing a protective headband for soccer initially.
Corvell is focused on designing and developing head protection products to reduce the likelihood of concussion when playing sports. Exploring and understanding medical insights, material science research, current and former players experiences and governing bodies guidelines has allowed Corvell to develop the safety, style, form and function requirements of a suitable product to bring to market.
Target Market(s)
Mums buying kits for the sons and daughters. Amateur footballers.
Industry/Entity Type
Sporting Good
Contact Information for Business Card
Martin Ashgrove - CEO
Mobile: +44 7391608254
Email: martin@corvell.co.uk
Tel: 0208 5143927
Helena Pardoe - COO
Mob: +44 7356 409183
Email: helena@corvell.co.uk
Tel: 0208 5143927
Duncan Wyvern - CCO
Mob: +44 7468 230517
Email: duncan@corvell.co.uk
Tel: 0208 5143927
Look and feel

```html
<!DOCTYPE html>
<html lang="en">
<head>
<meta charset="utf-8">
<title>Corvell Business Card</title>
<link rel="stylesheet" href="https://fonts.googleapis.com/css2?family=Roboto:wght@400;500;700&display=swap">
<style>
  :root {
    --backdrop: #3b3531;
    --card: #0d0d0f;
    --brand-blue: #1f6aa8;
    --ink: #f2f2f2;
  }
  * { margin: 0; padding: 0; box-sizing: border-box; }
  html, body {
    width: 1200px; height: 716px; overflow: hidden;
    background: var(--backdrop);
    font-family: "Roboto", Arial, sans-serif;
  }
  .sheet {
    width: 1200px; height: 716px;
    display: flex; align-items: center; justify-content: center; gap: 40px;
  }
  .card {
    width: 540px; height: 309px;
    background: var(--card);
    position: relative;
    box-shadow: 0 12px 30px rgba(0,0,0,0.45);
  }
  .card-front {
    display: flex; align-items: center; justify-content: center;
  }
  .wordmark {
    color: var(--ink);
    font-weight: 500;
    font-size: 50px;
    letter-spacing: 3px;
    text-transform: uppercase;
  }
  .card-back .identity {
    position: absolute;
    right: 290px; top: 128px;
    text-align: right;
  }
  .identity .name {
    color: var(--brand-blue);
    font-weight: 700;
    font-size: 15px;
    letter-spacing: 1.5px;
    text-transform: uppercase;
  }
  .identity .role {
    color: var(--ink);
    font-size: 11px;
    margin-top: 8px;
    letter-spacing: 0.5px;
  }
  .divider {
    position: absolute;
    left: 262px; top: 138px;
    width: 1px; height: 42px;
    background: var(--ink);
  }
  .contacts {
    position: absolute;
    left: 278px; top: 138px;
    list-style: none;
  }
  .contacts li {
    display: flex; align-items: center; gap: 6px;
    color: var(--ink);
    font-size: 11px;
    line-height: 14px;
    letter-spacing: 0.3px;
  }
  .contacts svg { width: 9px; height: 9px; fill: var(--brand-blue); flex: none; }
</style>
</head>
<body>
<main class="sheet">
  <section class="card card-front" aria-label="Card front">
    <span class="wordmark">Corvell</span>
  </section>

  <section class="card card-back" aria-label="Card back">
    <div class="identity">
      <p class="name">Martin Ashgrove</p>
      <p class="role">CEO</p>
    </div>
    <span class="divider"></span>
    <ul class="contacts">
      <li>
        <svg viewBox="0 0 10 10" aria-hidden="true"><path d="M2 0.5 L3.6 0.5 L4.2 2.8 L3 3.6 Q4 5.8 6.4 7 L7.2 5.8 L9.5 6.4 L9.5 8 Q9.5 9.5 8 9.5 Q0.5 9 0.5 2 Q0.5 0.5 2 0.5 Z"/></svg>
        0208 5143927
      </li>
      <li>
        <svg viewBox="0 0 10 10" aria-hidden="true"><path d="M2.5 0 H7.5 Q8.2 0 8.2 0.7 V9.3 Q8.2 10 7.5 10 H2.5 Q1.8 10 1.8 9.3 V0.7 Q1.8 0 2.5 0 Z M2.8 1.2 V8 H7.2 V1.2 Z"/></svg>
        +44 7391608254
      </li>
      <li>
        <svg viewBox="0 0 10 10" aria-hidden="true"><path d="M0 2 H10 V8.5 H0 Z M0.6 2.4 L5 5.6 L9.4 2.4 Z" fill-rule="evenodd"/></svg>
        martin@corvell.co.uk
      </li>
    </ul>
  </section>
</main>
</body>
</html>
```